Design the app for the next Dwelvo

We need a cutting edge, super UX-intuitive, design for a global parking app called Sloto.
- Homescreen and website have been finalised already (see attached pdf)
- Wireframed screens for the concepts we need have been provided in the attached pdf
- We need some really nice icons for parking space types, etc
- Needs to be very, very intuitive to use and navigate.
References: Dwelvo app & Zipto app, for their simplicity of use
Reason: A few designers have requested that we extend this deadline. So here you go.
Parking

```html
<!DOCTYPE html>
<html lang="en">
<head>
<meta charset="utf-8">
<title>Sloto – app screens</title>
<link href="https://fonts.googleapis.com/css2?family=Roboto:wght@300;400;500;700;900&display=swap" rel="stylesheet">
<style>
:root{
  --ink:#0d0d0d;
  --page:#ffffff;
  --brand:#cf4b50;
  --text-light:#f2f2f2;
  --rule:#3a3a3a;
  --map-base:#d9d9d9;
  --map-road:#efefef;
  --band:#3b3b3b;
}
*{box-sizing:border-box;margin:0;padding:0}
html,body{width:1200px;height:778px;overflow:hidden;background:var(--page)}
body{position:relative;font-family:"Roboto",Arial,sans-serif;color:var(--text-light)}
.screen{position:absolute;top:64px;background:var(--ink);overflow:hidden}
.screen--welcome{left:69px;width:300px;height:534px}
.screen--how{left:434px;width:282px;height:640px}
.screen--find{left:781px;width:300px;height:534px}

/* brand block: plain square above the name */
.brand{position:absolute;display:flex;flex-direction:column;font-family:"Roboto",Arial,sans-serif;font-weight:400;color:var(--text-light);text-transform:uppercase;line-height:1}
.brand__mark{display:block;background:var(--text-light);border-radius:5px}

/* welcome */
.hero{position:absolute;left:0;top:0;width:300px;height:366px;background:linear-gradient(160deg,#5a5a5a 0%,#3a3a3a 45%,#1f1f1f 100%)}
.hero .brand{left:0;right:0;top:106px;align-items:center;gap:22px;font-size:30px;letter-spacing:14px;padding-left:14px}
.hero .brand__mark{width:108px;height:108px;border-radius:8px}
.hero__tagline{position:absolute;left:0;right:0;top:288px;text-align:center;font-weight:300;font-size:15px}
.btn{position:absolute;display:flex;align-items:center;justify-content:center;background:var(--brand);color:#fff;border-radius:22px;font-family:"Roboto",Arial,sans-serif;font-weight:500;font-size:11px;text-transform:uppercase}
.btn--lease{left:40px;top:403px;width:213px;height:43px}
.btn--search{left:40px;top:452px;width:213px;height:43px}

/* header for inner screens */
.app-header{position:absolute;left:0;top:0;width:100%;height:114px;background:var(--ink)}
.app-header .brand{align-items:flex-start;gap:12px;font-size:12px;letter-spacing:5px}
.screen--how .app-header .brand{left:20px;top:26px}
.screen--how .app-header .brand__mark{width:47px;height:46px}
.screen--find .app-header .brand{left:22px;top:27px}
.screen--find .app-header .brand__mark{width:49px;height:49px}
.app-header__tagline{position:absolute;font-weight:300;font-size:14px;white-space:nowrap}
.screen--how .app-header__tagline{left:89px;top:52px}
.screen--find .app-header__tagline{left:95px;top:56px;font-size:15px}

/* how it works */
.how__title{position:absolute;left:21px;top:113px;font-weight:900;font-size:17px;text-transform:uppercase}
.rule{position:absolute;left:19px;width:247px;height:1px;background:var(--rule)}
.step__icon{position:absolute;left:38px;width:40px;height:48px}
.step__title{position:absolute;left:91px;font-weight:400;font-size:18px;line-height:16px;text-transform:uppercase}
.step__text{position:absolute;left:91px;width:170px;font-size:10.5px;line-height:14.4px}
.btn--start{left:38px;top:569px;width:200px;height:39px}

/* find */
.search-band{position:absolute;left:0;top:114px;width:300px;height:47px;background:var(--band)}
.search-field{position:absolute;left:21px;top:8px;width:250px;height:30px;border-radius:15px;background:#fff;color:#111;font-size:11.5px;display:flex;align-items:center;justify-content:center}
.map{position:absolute;left:0;top:161px;width:300px;height:304px;background:linear-gradient(135deg,var(--map-road) 0%,var(--map-base) 60%,#cfcfcf 100%)}
.map__pin{position:absolute;width:22px;height:30px}
.tabbar{position:absolute;left:0;top:465px;width:300px;height:69px;background:var(--brand);display:flex}
.tab{flex:1;display:flex;flex-direction:column;align-items:center;justify-content:center;gap:4px;border-left:1px solid rgba(255,255,255,.45);font-weight:500;font-size:9.5px;text-transform:uppercase;text-align:center;line-height:11px;color:#fff}
.tab:first-child{border-left:none}
.tab svg{width:22px;height:22px}
</style>
</head>
<body>

<section class="screen screen--welcome">
  <div class="hero" role="img" aria-label="Aerial black-and-white photo of city skyscrapers">
    <div class="brand"><span class="brand__mark"></span>Sloto</div>
    <p class="hero__tagline">Your private parking space</p>
  </div>
  <a class="btn btn--lease">Lease your parking space</a>
  <a class="btn btn--search">Search for parking</a>
</section>

<section class="screen screen--how">
  <header class="app-header">
    <div class="brand"><span class="brand__mark"></span>Sloto</div>
    <p class="app-header__tagline">Your private parking space</p>
  </header>
  <h2 class="how__title">How it works</h2>
  <div class="rule" style="top:145px"></div>

  <svg class="step__icon" style="top:160px" viewBox="0 0 40 48">
    <path d="M20 2a12 12 0 0 0-12 12c0 9 12 20 12 20s12-11 12-20A12 12 0 0 0 20 2z" fill="var(--brand)"/>
    <circle cx="20" cy="14" r="5" fill="var(--ink)"/><circle cx="20" cy="14" r="2.5" fill="var(--brand)"/>
    <path d="M10 46v-8l3-6h14l3 6v8h-4v-2H14v2z" fill="var(--brand)"/>
    <circle cx="14" cy="40" r="1.8" fill="var(--ink)"/><circle cx="26" cy="40" r="1.8" fill="var(--ink)"/>
  </svg>
  <h3 class="step__title" style="top:164px">Locate an<br>affordable<br>parking space<br>near you</h3>
  <p class="step__text" style="top:238px">Find someone who has an empty space where you can park your car, motorbike, boat or helicopter. This might be an empty driveway, a garage, a boat mooring or even a building rooftop</p>
  <div class="rule" style="top:336px"></div>

  <svg class="step__icon" style="top:354px" viewBox="0 0 40 48">
    <rect x="3" y="6" width="26" height="26" rx="2" fill="none" stroke="var(--brand)" stroke-width="2.5"/>
    <path d="M3 12h26" stroke="var(--brand)" stroke-width="4"/>
    <path d="M9 3v6M23 3v6" stroke="var(--brand)" stroke-width="2.5"/>
    <circle cx="27" cy="30" r="9" fill="var(--ink)" stroke="var(--brand)" stroke-width="2.5"/>
    <path d="M27 25v5l3 3" fill="none" stroke="var(--brand)" stroke-width="2"/>
  </svg>
  <h3 class="step__title" style="top:352px">Select your<br>booking time<br>and dates</h3>
  <p class="step__text" style="top:407px">Check availability, confirm the cost, then pay through Sloto.</p>
  <div class="rule" style="top:448px"></div>

  <svg class="step__icon" style="top:454px" viewBox="0 0 40 48">
    <circle cx="8" cy="10" r="7" fill="var(--brand)"/>
    <text x="8" y="13.5" font-size="9" font-family="Roboto,Arial,sans-serif" font-weight="700" fill="#fff" text-anchor="middle">P</text>
    <path d="M8 17v20" stroke="var(--brand)" stroke-width="2"/>
    <path d="M13 36v-7l3-7h16l3 7v7h-4v-2H17v2z" fill="var(--brand)"/>
    <circle cx="18" cy="30" r="1.8" fill="var(--ink)"/><circle cx="30" cy="30" r="1.8" fill="var(--ink)"/>
  </svg>
  <h3 class="step__title" style="top:464px">Park<br>your vehicle</h3>
  <p class="step__text" style="top:505px">Save time. Spend less. Sleep easy. Your vehicle now has its own private parking space.</p>

  <a class="btn btn--start">Start parking now</a>
</section>

<section class="screen screen--find">
  <header class="app-header">
    <div class="brand"><span class="brand__mark"></span>Sloto</div>
    <p class="app-header__tagline">Your private parking space</p>
  </header>
  <div class="search-band"><div class="search-field">48 Harbor Ln</div></div>
  <div class="map" role="img" aria-label="Grey street map of the neighbourhood with available parking spaces">
    <svg class="map__pin" style="left:182px;top:72px" viewBox="0 0 22 30"><path d="M11 1a10 10 0 0 0-10 10c0 7 10 18 10 18s10-11 10-18A10 10 0 0 0 11 1z" fill="var(--brand)"/><circle cx="11" cy="11" r="4" fill="#fff"/></svg>
    <svg class="map__pin" style="left:132px;top:171px" viewBox="0 0 22 30"><path d="M11 1a10 10 0 0 0-10 10c0 7 10 18 10 18s10-11 10-18A10 10 0 0 0 11 1z" fill="var(--brand)"/><circle cx="11" cy="11" r="4" fill="#fff"/></svg>
    <svg class="map__pin" style="left:178px;top:197px" viewBox="0 0 22 30"><path d="M11 1a10 10 0 0 0-10 10c0 7 10 18 10 18s10-11 10-18A10 10 0 0 0 11 1z" fill="var(--brand)"/><circle cx="11" cy="11" r="4" fill="#fff"/></svg>
  </div>
  <nav class="tabbar">
    <div class="tab"><svg viewBox="0 0 22 22"><circle cx="8" cy="8" r="6" fill="none" stroke="#fff" stroke-width="2.5"/><path d="M12.5 12.5l7 6" stroke="#fff" stroke-width="3"/></svg>Find<br>a space</div>
    <div class="tab"><svg viewBox="0 0 22 22"><rect x="2" y="4" width="18" height="16" rx="1.5" fill="none" stroke="#fff" stroke-width="2"/><path d="M2 8h18" stroke="#fff" stroke-width="3"/><path d="M6 2v4M16 2v4" stroke="#fff" stroke-width="2"/><path d="M5 12h2M10 12h2M15 12h2M5 16h2M10 16h2M15 16h2" stroke="#fff" stroke-width="2"/></svg>Bookings</div>
    <div class="tab"><svg viewBox="0 0 22 22"><rect x="2" y="2" width="5" height="5" fill="#fff"/><rect x="8.5" y="2" width="5" height="5" fill="#fff"/><rect x="15" y="2" width="5" height="5" fill="#fff"/><path d="M4.5 7v4h13V7M11 7v13M6 20h10" stroke="#fff" stroke-width="2" fill="none"/></svg>Your<br>spaces</div>
    <div class="tab"><svg viewBox="0 0 22 22"><circle cx="11" cy="5" r="3.5" fill="#fff"/><path d="M6 10h10v7h-2v4H8v-4H6z" fill="#fff"/></svg>Profile</div>
  </nav>
</section>

</body>
</html>
```